Spring 2026 Deck Construction Direct Mail Flier

The logo files I will include were named "maple ridge fixers" by the digital artist. However, my company is called Maple Ridge Yardworks (That was not a typo. There is no space between "home" and "service") If you'd like to experiment with color modification of the logo to make it fit better with designs you come up with, please be my guest.

I need a 6"x12" flier design to market my deck construction business. The expected goal is to get phone calls and book appointments for the upcoming Spring 2026 construction season. The call to action being something along the lines of "Call now; Appointments are going fast!"

My target audience is upper middle class (annual household income $100,000 - $200,000) families of 3-5 in the capital region of New York state, US. Houses are most commonly either vinyl sided, or sometimes a combination of vinyl siding and brick. The ideal flier design will feature this type of house. Also most houses in my target area have nice lawns with mulched gardens as well.

I prefer designs with more sweeping, gradual curves than sharp square edges and corners, though some squares and corners are ok. I like designs with pallets consisting of blue, red, green, black, gray. I do not like purple, pink, yellow, or orange.

If it's possible and will fit, it would be nice to have images of pressure treated lumber, western cedar decking, and composite decking, so that customers understand I can provide any of the three. Also listing them out would be great.

I prefer designs that are more visual than text-based. On at least one side the dominant element should be a visual of a large composite or cedar deck. An image somewhere - wherever it can fit - of a small (10'x14' or so), basic deck of pressure treated lumber would be ideal as well so that potential clients know I will build those. Also I would like some element, on either side, that creates a sense of urgency by drawing the eye to text along the lines of "2026 appointments are filling fast. Book your free consultation today!"

Selling points:
- Veteran owned and operated
- Hometown feel
- Personal service
- Satisfaction guaranteed

I will use the Northfield Parcel Bureau's "Bright Lane Route Mailer" (BLRM) service to deliver these, so on either the front or back there should be a small amount of reserved space in the top right corner for the NFPB's required markings (see https://www.larkstonepromo.com/products/plumber-fixit-blrm-postcard?variant=17305529816 for an example of the amount of space required). It's ok if there is imagery there and it gets covered up by the NFPB markings, it just shouldn't be anything important. You do not have to include the NFPB markings themselves. My print guy will do that when I pass him this design.

A final note on this; I've mentioned Spring 2026 several times. But I do not want the design to be relevant only for Spring. I'd like to use the design throughout the year so please no hard references to Spring that will make the flier seem out of place in the fall.

Thank you very much. I appreciate your time.

```html
<!DOCTYPE html>
<html lang="en">
<head>
<meta charset="utf-8">
<title>Maple Ridge Yardworks – Deck Construction Mailer</title>
<link href="https://fonts.googleapis.com/css2?family=Montserrat:wght@300;400;500;600;700;800&display=swap" rel="stylesheet">
<style>
  :root{
    --navy:#0b2b4f;
    --red:#b01e23;
    --white:#ffffff;
    --ink:#141414;
    --stage:#8a8a8a;
    --sky-top:#3f7fd0;
    --sky-bottom:#d9c9ad;
  }
  *{margin:0;padding:0;box-sizing:border-box}
  html,body{width:1083px;height:1200px;overflow:hidden;background:var(--stage)}
  body{position:relative;font-family:"Montserrat",Arial,sans-serif;color:var(--ink)}
  .card{position:absolute;left:82.3px;width:1272px;height:635px;background:var(--white);
        transform-origin:0 0;transform:scale(.7222);overflow:hidden;box-shadow:0 4px 10px rgba(0,0,0,.35)}
  .card--front{top:88px}
  .card--back{top:599.5px}
  .shapes{position:absolute;inset:0;width:1272px;height:635px}
  .abs{position:absolute}
  .white{color:var(--white)}

  /* brand mark */
  .brand{position:absolute;display:flex;flex-direction:column;align-items:center;text-align:center;gap:6px}
  .brand__dot{width:52px;height:52px;border-radius:50%;border:5px solid var(--navy)}
  .brand__name{font-weight:700;font-size:15px;line-height:1.15;color:var(--navy)}

  /* front */
  .headline{left:616px;top:32px;font-size:38px;line-height:37px;font-weight:500;color:var(--navy)}
  .headline b{color:var(--red);font-weight:800}
  .headline .dot{font-weight:800}
  .lede{left:614px;top:110px;width:560px;font-size:17px;line-height:21px;font-weight:500}
  .tile{position:absolute;top:170px;width:232px;height:148px;border:3px solid var(--navy);border-radius:10px;overflow:hidden;background:var(--navy)}
  .tile__photo{height:103px}
  .tile__label{height:42px;display:flex;align-items:center;justify-content:center;text-align:center;color:var(--white);font-size:18px;line-height:17px;font-weight:500}
  .perk{position:absolute;top:326px;width:200px;text-align:center;font-size:17px;line-height:21px;font-weight:500}
  .perk__icon{width:54px;height:54px;margin:0 auto 12px;display:block}
  .perk__rule{position:absolute;top:340px;width:2px;height:95px;background:var(--red)}
  .urgent{left:50px;top:492px;font-size:35px;font-weight:400;color:var(--white)}
  .pill{position:absolute;background:var(--red);color:var(--white);font-weight:700;border-radius:9px;display:flex;align-items:center;justify-content:center}
  .pill--book{left:48px;top:536px;width:587px;height:50px;font-size:34px}
  .split{position:absolute;left:658px;top:497px;width:2px;height:86px;background:rgba(255,255,255,.45)}
  .call{position:absolute;display:flex;align-items:center;gap:12px;color:var(--white)}
  .call--front{left:692px;top:498px}
  .call--front .call__lead{font-size:40px;font-weight:700}
  .call--front .call__num{font-size:40px;font-weight:400}
  .serve{font-size:13.5px;letter-spacing:.9px;font-weight:500;color:var(--white)}
  .serve--front{left:688px;top:546px}
  .site--front{left:746px;top:562px;font-size:21px;letter-spacing:1.4px;color:var(--white);font-weight:500}

  /* back */
  .back-title{left:50px;top:52px;font-size:31px;font-weight:700}
  .back-title span{font-weight:400}
  .back-copy{left:52px;top:100px;width:790px;font-size:16px;line-height:20px;font-weight:400}
  .postal{position:absolute;left:1013px;width:216px;border:2px solid #111;font-family:Arial,Helvetica,sans-serif;color:#222;text-align:center}
  .postal--indicia{top:18px;height:89px;padding-top:7px;font-size:15px;line-height:18px;font-weight:700}
  .postal--indicia .big{font-size:21px;line-height:26px}
  .postal--addressee{top:117px;height:70px;text-align:left;padding:14px 0 0 14px;font-size:15px;line-height:19px;font-weight:700}
  .other{left:65px;top:212px;font-size:29px;font-weight:700;color:var(--red)}
  .svc{position:absolute;left:63px;display:flex;align-items:center;gap:17px;font-size:23px;font-weight:700}
  .svc svg{width:33px;height:33px}
  .tagline{left:66px;top:400px;font-size:17.5px;font-weight:700}
  .rush{left:52px;top:463px;font-size:37px;font-weight:700;color:var(--white)}
  .schedule{left:48px;top:512px;display:flex;align-items:center;gap:12px}
  .schedule__lead{font-size:34px;font-weight:400;color:var(--white)}
  .schedule__box{background:var(--navy);color:var(--white);font-size:33px;font-weight:700;padding:2px 14px 4px 9px}
  .serve--back{left:52px;top:566px;font-size:17px;letter-spacing:1.6px}
  .pill--build{left:753px;top:214px;width:255px;height:44px;font-size:29px;border-radius:7px}
  .material{position:absolute;left:752px;color:var(--white)}
  .material__name{display:flex;align-items:center;gap:14px;font-size:27px;font-weight:700}
  .material__name svg{width:22px;height:22px}
  .material__note{padding-left:37px;font-size:21px;font-weight:400;margin-top:2px}
  .call--back{left:813px;top:520px}
  .call--back .call__lead{font-size:32px;font-weight:400}
  .call--back .call__num{font-size:28px;font-weight:500}
  .site--back{left:813px;top:563px;font-size:21px;font-weight:700;color:var(--white)}
</style>
</head>
<body>

<!-- FRONT -->
<section class="card card--front">
  <svg class="shapes" viewBox="0 0 1272 635" aria-hidden="false">
    <defs>
      <linearGradient id="houseTone" x1="0" y1="0" x2="0" y2="1">
        <stop offset="0" stop-color="#3f7fd0"/>
        <stop offset=".45" stop-color="#8fb3de"/>
        <stop offset="1" stop-color="#c8b89a"/>
      </linearGradient>
    </defs>
    <path role="img" aria-label="Photo of a two-storey sided house under construction with ladders and scaffolding"
          d="M0 0 H345 C450 90 480 320 410 470 C260 440 100 400 0 350 Z" fill="url(#houseTone)"/>
    <path d="M0 350 C120 410 280 462 420 468 C700 476 1000 462 1272 440 V635 H0 Z" fill="var(--navy)"/>
    <path d="M410 468 C700 474 1000 460 1272 441" fill="none" stroke="var(--red)" stroke-width="6"/>
    <path d="M336 -4 C446 88 480 320 406 472" fill="none" stroke="var(--red)" stroke-width="10"/>
  </svg>

  <div class="brand" style="left:462px;top:36px;width:120px">
    <span class="brand__dot"></span>
    <span class="brand__name">Maple Ridge<br>Yardworks</span>
  </div>

  <h1 class="abs headline">Your Home<span class="dot">.</span> <b>Our Expertise.</b><br><b>Premium Deck</b> Construction</h1>
  <p class="abs lede">Custom decks that expand your living space and enhance enjoyment of your backyard.</p>

  <div class="tile" style="left:480px">
    <div class="tile__photo" role="img" aria-label="Composite deck beside a pool with lounge chairs" style="background:linear-gradient(100deg,#49b6e0 0%,#8fd3ea 30%,#b56e45 55%,#8d4e2f 100%)"></div>
    <div class="tile__label">Composite</div>
  </div>
  <div class="tile" style="left:732px">
    <div class="tile__photo" role="img" aria-label="Western cedar deck walkway with rope railing beside a lawn" style="background:linear-gradient(100deg,#8b5a34 0%,#a46a3d 40%,#6fae3a 60%,#4f8f2a 100%)"></div>
    <div class="tile__label">Western Cedar</div>
  </div>
  <div class="tile" style="left:983px">
    <div class="tile__photo" role="img" aria-label="Stacked pressure treated lumber boards" style="background:linear-gradient(120deg,#c98a66,#b06f4d 50%,#d49d7b)"></div>
    <div class="tile__label">Pressure<br>Treated Lumber</div>
  </div>

  <div class="perk" style="left:457px">
    <svg class="perk__icon" viewBox="0 0 54 54"><circle cx="27" cy="27" r="27" fill="var(--red)"/><path d="M27 38 L15 26 a6 6 0 0 1 12-6 a6 6 0 0 1 12 6 Z" fill="#fff"/></svg>
    Local, Veteran-Owned Craftsmanship
  </div>
  <span class="perk__rule" style="left:668px"></span>
  <div class="perk" style="left:665px">
    <svg class="perk__icon" viewBox="0 0 54 54"><circle cx="27" cy="27" r="27" fill="var(--red)"/><rect x="17" y="13" width="18" height="24" rx="2" fill="#fff"/><path d="M21 20h10M21 25h10M21 30h6" stroke="var(--red)" stroke-width="2"/><circle cx="36" cy="36" r="5" fill="#fff"/></svg>
    Licensed &amp; Insured Professionals
  </div>
  <span class="perk__rule" style="left:872px"></span>
  <div class="perk" style="left:874px">
    <svg class="perk__icon" viewBox="0 0 54 54"><circle cx="27" cy="27" r="27" fill="var(--red)"/><path d="M14 27 L27 15 L40 27 V39 H14 Z" fill="#fff"/><path d="M21 29 l4 4 l8-8" fill="none" stroke="var(--red)" stroke-width="3"/></svg>
    Quality Work You Can Rely On
  </div>
  <span class="perk__rule" style="left:1081px"></span>
  <div class="perk" style="left:1054px;top:326px">
    <svg class="perk__icon" viewBox="0 0 54 54"><circle cx="27" cy="27" r="27" fill="var(--red)"/><circle cx="27" cy="23" r="9" fill="none" stroke="#fff" stroke-width="3"/><path d="M23 23 l3 3 l5-6" fill="none" stroke="#fff" stroke-width="2.5"/><path d="M13 38 h28" stroke="#fff" stroke-width="3"/></svg>
    Satisfaction Guaranteed
  </div>

  <p class="abs urgent">2026 appointment slots filling fast</p>
  <div class="pill pill--book">Book your free consultation now</div>
  <span class="split"></span>

  <div class="call call--front">
    <span class="call__lead">Call Today</span>
    <svg width="32" height="32" viewBox="0 0 32 32"><circle cx="16" cy="16" r="15" fill="var(--red)"/><path d="M11 8 l4 4 l-2 2 a10 10 0 0 0 5 5 l2-2 l4 4 l-2 3 c-8 0-14-6-14-14 Z" fill="#fff"/></svg>
    <span class="call__num">(518) 555-0147</span>
  </div>
  <p class="abs serve serve--front">Serving the Capital Region with trusted deck design and construction.</p>
  <p class="abs site--front">www.mapleridgeyardworks.com</p>
</section>

<!-- BACK -->
<section class="card card--back">
  <svg class="shapes" viewBox="0 0 1272 635">
    <defs>
      <linearGradient id="techTone" x1="0" y1="0" x2="1" y2="1">
        <stop offset="0" stop-color="#d9d4cc"/><stop offset=".6" stop-color="#b9a68c"/><stop offset="1" stop-color="#7b8a3a"/>
      </linearGradient>
      <linearGradient id="repairTone" x1="0" y1="0" x2="1" y2="1">
        <stop offset="0" stop-color="#d6c3ad"/><stop offset=".5" stop-color="#4f6f99"/><stop offset="1" stop-color="#8a4e2a"/>
      </linearGradient>
    </defs>
    <path d="M720 192 C900 182 1100 192 1272 218 V635 H830 C780 590 745 520 730 440 C725 360 726 260 720 192 Z" fill="var(--navy)"/>
    <path d="M0 442 C250 452 500 456 712 440 C742 520 780 590 830 635 H0 Z" fill="var(--red)"/>
    <path d="M0 210 C300 190 600 178 830 182 C1000 186 1150 200 1272 216" fill="none" stroke="var(--red)" stroke-width="5"/>
    <circle role="img" aria-label="Smiling electrician in hard hat working on a wiring panel" cx="420" cy="250" r="95" fill="url(#techTone)"/>
    <circle role="img" aria-label="Worker kneeling to repair a damaged wall with tools on the floor" cx="613" cy="307" r="125" fill="url(#repairTone)" stroke="#fff" stroke-width="5"/>
  </svg>

  <h2 class="abs back-title">Decks Built Better Tailored to <span>Your Home &amp; Lifestyle</span></h2>
  <p class="abs back-copy">At Maple Ridge Yardworks, our team brings 23+ years of experience and has completed 500+ projects across Clifton Park and the Capital Region, helping over 1,000 homeowners improve and protect their homes.</p>

  <div class="brand" style="left:878px;top:64px;width:110px">
    <span class="brand__dot"></span>
    <span class="brand__name">Maple Ridge<br>Yardworks</span>
  </div>

  <div class="postal postal--indicia">PRESORTED STANDARD<br>NFPB POSTAGE PAID<br>2BRIGHTLANE<br><span class="big">ECRWSS</span></div>
  <div class="postal postal--addressee">LOCAL<br>POSTAL CUSTOMER</div>

  <p class="abs other">Other services</p>
  <div class="svc" style="top:262px">
    <svg viewBox="0 0 33 33"><circle cx="16.5" cy="16.5" r="16.5" fill="var(--navy)"/><path d="M18 6 L10 18 H16 L14 27 L23 14 H17 Z" fill="#fff"/></svg>Electrical
  </div>
  <div class="svc" style="top:310px">
    <svg viewBox="0 0 33 33"><circle cx="16.5" cy="16.5" r="16.5" fill="var(--navy)"/><path d="M9 21 h15 M9 17 h15 M10 13 h13 M11 21 v5 M22 21 v5" stroke="#fff" stroke-width="2"/></svg>Deck Building
  </div>
  <div class="svc" style="top:357px">
    <svg viewBox="0 0 33 33"><circle cx="16.5" cy="16.5" r="16.5" fill="var(--navy)"/><path d="M16.5 7 C20 13 23 16 23 20 a6.5 6.5 0 0 1 -13 0 C10 16 13 13 16.5 7 Z" fill="#fff"/></svg>House &amp; Roof Soft Wash
  </div>
  <p class="abs tagline">Fast turnaround without compromising quality</p>

  <p class="abs rush">2026 appointment slots filling fast</p>
  <div class="abs schedule"><span class="schedule__lead">Schedule your</span><span class="schedule__box">FREE on-site consultation</span></div>
  <p class="abs serve serve--back">Serving the Capital Region with trusted deck design and construction.</p>

  <div class="pill pill--build">We Build With</div>
  <div class="material" style="top:278px">
    <div class="material__name"><svg viewBox="0 0 22 22"><circle cx="11" cy="11" r="9" fill="none" stroke="#fff" stroke-width="2"/><path d="M7 11 l3 3 l6-6" fill="none" stroke="#fff" stroke-width="2"/></svg>Premium Composite</div>
    <div class="material__note">Long-lasting and low maintenance</div>
  </div>
  <div class="material" style="top:355px">
    <div class="material__name"><svg viewBox="0 0 22 22"><circle cx="11" cy="11" r="9" fill="none" stroke="#fff" stroke-width="2"/><path d="M7 11 l3 3 l6-6" fill="none" stroke="#fff" stroke-width="2"/></svg>Western Cedar</div>
    <div class="material__note">Classic, rich natural wood beauty</div>
  </div>
  <div class="material" style="top:432px">
    <div class="material__name"><svg viewBox="0 0 22 22"><circle cx="11" cy="11" r="9" fill="none" stroke="#fff" stroke-width="2"/><path d="M7 11 l3 3 l6-6" fill="none" stroke="#fff" stroke-width="2"/></svg>Pressure-Treated Lumber</div>
    <div class="material__note">strong, dependable for any budget</div>
  </div>

  <div class="call call--back">
    <span class="call__lead">Call Today</span>
    <svg width="28" height="28" viewBox="0 0 32 32"><circle cx="16" cy="16" r="15" fill="var(--red)"/><path d="M11 8 l4 4 l-2 2 a10 10 0 0 0 5 5 l2-2 l4 4 l-2 3 c-8 0-14-6-14-14 Z" fill="#fff"/></svg>
    <span class="call__num">(518) 555-0147</span>
  </div>
  <p class="abs site--back">www.mapleridgeyardworks.com</p>
</section>

</body>
</html>
```